We need a book cover for a novel called "Eleven Lanterns".

In essence it is a novel about a girl, Mira Dunholt, who owns an Antique Shop, The Brass Lantern Emporium, in modern day London. She buys the contents of the deceased estate of Harriet Penrose. Amongst that estate is a box of old English postcards, each postcard providing a snippet of life in London during WWII, all signed by the mysterious "B", and all addressed to "Phil". Whilst Mira is cleaning and pricing some of the belongings from that estate she is unexpectedly transported back in time. She ends up in New Zealand in 1860 at the time of the gold rush; in India in 1856, just as the Indian Revolt occurs; in London in 1896 staying at the Carlmont hotel, and again in London during the Blitz.
This is the Heirloom Hunters Hour woven into the pages of a book as you follow the journey of silver, rubies and diamonds, greenstone and tiger knives (Katar). A novel where tiger hunts and ruby necklaces are entwined with murders and maids.
Each story forms part of the story of Harriet Penrose and the history of her family.
The different stories are magically woven together into a climatic ending, involving auction houses, deadly collectors, and love.

Below is the blurb for the back cover:

"Following the unexplained disappearance of her parents, and in a last ditch attempt to save the antique store she has inherited from financial ruin, Mira Dunholt takes on a deceased estate. Amongst the estate is a collection of fifteen vintage postcards.

Mira is unprepared for the enigma these postcards hint at about their reclusive former owner. They consume her and complicate her life in unimaginable ways.

A novel traversing three continents, and two centuries, where tiger hunts and ruby necklaces are irrevocably entwined with murders and mysteries, auction houses and antiquities.

It might also explain what happened to her parents ..."

This is the Pinterest board with some images on it which capture the essence of the book. http://www.pinboardia.example/tuivdrgr/possible-book-cover-inspirations/

The authors name is Rowena Tallard. Below is the blurb about the author to be included on the back cover:

"Rowena Tallard has worked in her family's antique store since she was a toddler.
She’s gone from being allowed to sell 50c postcards in the corner of Relic Lane, a literal treasure trove, to selling $5,000 Worcester vases at prestigious antique fairs around New Zealand.
She lives in Auckland with her husband and two daughters."

Just added the "blurb" for the back of the book to the brief. Thank you.

Added the Author Blurb to the design brief and a few more images of stamps & postmarks for reference.

Just amended the blurb. Thanks. Last change.

Just updated the blurb and the author's blurb for the back cover in the brief. Please use this latest version. Also loaded an image of the author for the back cover. Please incorporate this in your design for the back cover (not too large though). Thank you so very much.

Target Market(s)

The target reader is a woman, but ideally the cover shouldn't be too feminine.

Industry/Entity Type

Financial

Font styles to use
Script

Requirements
Must have
• Author's name at the bottom, centre. In a plain font.
Nice to have
• A postmark or a stamp or an old postcard/letter image somewhere.
Should not have
• No feather quills.

```html
<!DOCTYPE html>
<html lang="en">
<head>
<meta charset="utf-8">
<title>Eleven Lanterns — Book Cover</title>
<link rel="stylesheet" href="https://fonts.googleapis.com/css2?family=Cinzel:wght@500&family=Dancing+Script:wght@600&display=swap">
<style>
  :root {
    --backdrop: #8a8275;
    --paper-light: #d9b878;
    --paper-mid: #c49a55;
    --paper-dark: #8f6a33;
    --fold: rgba(90, 60, 25, 0.35);
    --title-red: #7a2328;
    --author-ink: #3d2a1c;
    --stamp-pink: #d98a80;
    --stamp-edge: #f1e2cc;
    --postmark-ink: rgba(40, 30, 25, 0.75);
  }
  html, body {
    margin: 0;
    padding: 0;
    width: 1200px;
    height: 900px;
    overflow: hidden;
    background: var(--backdrop);
  }
  .canvas {
    position: relative;
    width: 1200px;
    height: 900px;
  }
  .book-cover {
    position: absolute;
    left: 290px;
    top: 20px;
    width: 620px;
    height: 860px;
    overflow: hidden;
    background:
      linear-gradient(90deg, rgba(80,50,20,0.45) 0, rgba(80,50,20,0.1) 14px, rgba(255,240,200,0.12) 22px, transparent 40px),
      radial-gradient(ellipse at 50% 45%, var(--paper-light) 0%, var(--paper-mid) 65%, var(--paper-dark) 100%);
  }
  .fold-line {
    position: absolute;
    left: 352px;
    top: 0;
    width: 3px;
    height: 100%;
    background: linear-gradient(90deg, transparent, var(--fold), transparent);
  }
  .postmark {
    position: absolute;
    left: 222px;
    top: 30px;
    width: 126px;
    height: 126px;
  }
  .stamp {
    position: absolute;
    left: 453px;
    top: 48px;
    width: 130px;
    height: 88px;
    background: var(--stamp-pink);
    border: 5px solid var(--stamp-edge);
    box-sizing: border-box;
  }
  .title {
    position: absolute;
    left: 0;
    top: 0;
    margin: 0;
    font-family: "Dancing Script", cursive;
    font-weight: 600;
    color: var(--title-red);
    line-height: 1;
  }
  .title-line {
    position: absolute;
    white-space: nowrap;
  }
  .title-line--first {
    left: 48px;
    top: 196px;
    font-size: 138px;
  }
  .title-line--second {
    left: 196px;
    top: 318px;
    font-size: 112px;
  }
  .author {
    position: absolute;
    left: 0;
    width: 100%;
    top: 748px;
    margin: 0;
    text-align: center;
    font-family: "Cinzel", serif;
    font-weight: 500;
    font-size: 38px;
    letter-spacing: 1px;
    color: var(--author-ink);
  }
</style>
</head>
<body>
<main class="canvas">
  <section class="book-cover">
    <div class="fold-line"></div>

    <svg class="postmark" viewBox="0 0 126 126" role="img" aria-label="Circular date postmark">
      <circle cx="63" cy="63" r="56" fill="none" stroke="var(--postmark-ink)" stroke-width="3"/>
      <circle cx="63" cy="63" r="40" fill="none" stroke="var(--postmark-ink)" stroke-width="1.5" stroke-dasharray="6 4"/>
    </svg>

    <div class="stamp" role="img" aria-label="Vintage postage stamp with wavy cancellation"></div>

    <h1 class="title">
      <span class="title-line title-line--first">Eleven</span>
      <span class="title-line title-line--second">Lanterns</span>
    </h1>

    <p class="author">Rowena Tallard</p>
  </section>
</main>
</body>
</html>
```